Sip. Stroll. Flourish. Book Cover

I would like a book cover for the print edition book I am self publishing. My cover will require front, back, and spine design. I have provided a template to assist with sizing and spacing.

My book is named "Sip. Stroll. Flourish. A Simple Diet, Drive to Stretch, and Outlook Manual Building Traction Along Better Vigor and Balance" by Gregory Talbrecht RD, CPT. I use the concept of waves as an analogy for forward progress in life and would like that reflected in the cover design. I would like the color scheme to be blacks, whites, grey, and various shades of blue. I have provided a style guide for reference. Please include my logo on the front, spine, and back of the design. Please include an about the author, book summary, and my picture on the back. I have provided the wording below.

About the Author: Gregory Talbrecht is a Registered Dietitian and Certified Personal Trainer from Cleveland, OH. He graduated from the Verdant Plains University and currently works as a health coach in the healthcare industry. His passions are fitness, nutrition, science, and motivation. He has extensive knowledge and experience in wellness, healthcare, and disease treatment and disease. Gregory has worked with hundreds of people through counseling, consulting, and coaching in an effort to make a difference in their long-term health. In his spare time, he enjoys exercising, watching movies, and trying out new foods.

Book Summary: Believe in you. Trust in You. Sip. Stroll. Flourish. is a book committed to you. Behavior change and improved health can be challenging. You must feel empowered to make decisions and changes create momentum in the right direction. But, you may not always have the knowledge to do that. This book provides you with practical and fun tools and tips to improve your nutrition, motivation to move, and mindset. You are awesome. You are beautiful. You have the power to control your destiny and future. All you have to do is Sip, Stroll, and Flourish!

Please use a modern/ futuristic font style for the title. I have also provided some draft book covers for inspiration/ direction. Thank you!

Colors

Designer to choose only greyscale colors for use in the design.

Requirements
Must have
• Color scheme, about author, profile picture, and book summary on back, wave themed graphics

```html
<!DOCTYPE html>
<html lang="en">
<head>
<meta charset="utf-8">
<title>Sip. Stroll. Flourish. — Book Cover</title>
<link rel="stylesheet" href="https://fonts.googleapis.com/css2?family=Orbitron:wght@700;900&family=Roboto:ital,wght@0,400;0,700;1,700&family=Lobster&family=Allura&display=swap">
<style>
  :root {
    --stage: #e6e6e8;
    --navy-top: #3b5283;
    --navy-mid: #34497a;
    --navy-deep: #22345e;
    --spine: #283c69;
    --ink-light: #f1f3f8;
    --ink-soft: #d9deea;
    --brand-blue: #1e7ad0;
    --tag-blue: #2a9be8;
    --snow-light: #c9d2e2;
    --snow-mid: #8e9fc0;
    --snow-dark: #4d6290;
    --photo-light: #cfcfcf;
    --photo-dark: #3a3a3a;
    --wave: #ffffff;
  }
  * { box-sizing: border-box; margin: 0; padding: 0; }
  html, body { width: 1200px; height: 989px; overflow: hidden; }
  body {
    background: var(--stage);
    font-family: "Roboto", Arial, sans-serif;
  }
  .book-spread {
    position: absolute;
    left: 116px; top: 114px;
    display: flex;
    height: 760px;
    box-shadow: 0 12px 30px rgba(0,0,0,.25);
  }
  .wave-lines {
    position: absolute; left: 0; width: 100%;
    pointer-events: none;
  }
  .wave-lines path { fill: none; stroke: var(--wave); }

  /* ---------- back cover ---------- */
  .back-cover {
    position: relative;
    width: 470px; height: 100%;
    background:
      radial-gradient(ellipse at 78% 62%, rgba(140,160,200,.35) 0%, rgba(140,160,200,0) 55%),
      linear-gradient(160deg, var(--navy-top) 0%, var(--navy-mid) 45%, var(--navy-deep) 100%);
    color: var(--ink-light);
    overflow: hidden;
  }
  .back-cover .wave-lines { top: 470px; height: 290px; }
  .back-cover__tagline {
    position: absolute; top: 64px; left: 0; width: 100%;
    text-align: center;
    font-family: "Lobster", cursive;
    font-weight: 400;
    font-size: 31px;
    color: var(--tag-blue);
    text-shadow: 0 1px 2px rgba(0,0,0,.35);
  }
  .back-cover__rule {
    position: absolute; top: 132px; left: 190px;
    width: 90px; height: 1px; background: var(--ink-soft);
  }
  .book-summary {
    position: absolute; top: 168px; left: 42px; width: 392px;
    font-size: 13px; line-height: 1.44;
    text-align: justify;
    color: var(--ink-light);
  }
  .author-photo {
    position: absolute; top: 398px; left: 40px;
    width: 144px; height: 208px;
    border: 2px solid #9aa3b5;
    background: radial-gradient(circle at 55% 40%, var(--photo-light) 0%, #8d8d8d 50%, var(--photo-dark) 100%);
  }
  .about-author {
    position: absolute; top: 394px; left: 196px; width: 240px;
  }
  .about-author__heading {
    font-style: italic; font-weight: 700;
    font-size: 15px;
    margin-bottom: 6px;
  }
  .about-author__body {
    font-size: 10.8px; line-height: 1.38;
    text-align: justify;
    color: var(--ink-soft);
  }
  .back-brand {
    position: absolute; left: 72px; top: 648px;
    display: flex; align-items: center; gap: 8px;
  }
  .brand-name {
    font-family: "Roboto", Arial, sans-serif;
    font-weight: 700;
    color: var(--brand-blue);
    letter-spacing: 1px;
  }
  .back-brand .brand-name { font-size: 36px; }
  .brand-square { width: 14px; height: 14px; background: var(--brand-blue); }
  .back-cover__url {
    position: absolute; left: 72px; top: 700px;
    font-style: italic; font-weight: 700;
    font-size: 12px;
    color: var(--ink-light);
  }
  .barcode-frame {
    position: absolute; left: 270px; top: 630px;
    width: 178px; height: 110px;
    border: 1px solid rgba(255,255,255,.3);
  }

  /* ---------- spine ---------- */
  .spine {
    position: relative;
    width: 28px; height: 100%;
    background: var(--spine);
    border-left: 1px solid rgba(0,0,0,.25);
    border-right: 1px solid rgba(255,255,255,.08);
  }
  .spine__brand, .spine__title, .spine__author {
    position: absolute; left: 50%;
    writing-mode: vertical-rl;
    transform: translateX(-50%);
    white-space: nowrap;
  }
  .spine__brand { top: 26px; font-size: 15px; }
  .spine__title {
    top: 84px;
    font-family: "Orbitron", sans-serif; font-weight: 700;
    font-size: 7px; letter-spacing: 1px;
    color: var(--brand-blue);
  }
  .spine__author {
    bottom: 30px;
    font-size: 11px; letter-spacing: 2px;
    color: var(--ink-soft);
  }

  /* ---------- front cover ---------- */
  .front-cover {
    position: relative;
    width: 470px; height: 100%;
    background: linear-gradient(180deg, var(--navy-top) 0%, var(--navy-mid) 45%, var(--navy-deep) 100%);
    overflow: hidden;
  }
  .front-cover__scene {
    position: absolute; left: 0; top: 200px;
    width: 100%; height: 560px;
    background:
      radial-gradient(circle at 18% 14%, rgba(255,255,255,.85) 0%, rgba(255,255,255,.25) 8%, rgba(255,255,255,0) 22%),
      radial-gradient(ellipse at 35% 40%, rgba(210,220,236,.45) 0%, rgba(210,220,236,0) 50%),
      linear-gradient(180deg, rgba(52,73,122,0) 0%, var(--snow-dark) 22%, var(--snow-mid) 42%, var(--snow-light) 58%, var(--snow-mid) 78%, var(--navy-deep) 100%);
  }
  .front-cover .wave-lines { top: 300px; height: 460px; }
  .front-brand { position: absolute; top: 28px; right: 28px; }
  .front-brand .brand-name { font-size: 30px; }
  .front-title {
    position: absolute; top: 66px; left: 38px;
    font-family: "Orbitron", sans-serif; font-weight: 900;
    line-height: 1.0;
    text-transform: uppercase;
    background: linear-gradient(180deg, #ffffff 0%, #c9ccd3 45%, #8d929c 55%, #eceef2 100%);
    -webkit-background-clip: text; background-clip: text;
    color: transparent;
    filter: drop-shadow(0 2px 2px rgba(0,0,0,.35));
  }
  .front-title span { display: block; }
  .front-title__line1 { font-size: 50px; letter-spacing: 6px; }
  .front-title__line2 { font-size: 50px; letter-spacing: 3px; }
  .front-title__line3 { font-size: 46px; letter-spacing: 1px; }
  .front-cover__author {
    position: absolute; bottom: 60px; left: 0; width: 100%;
    text-align: center;
    font-family: "Allura", cursive;
    font-size: 48px;
    color: var(--ink-light);
  }
</style>
</head>
<body>
  <main class="book-spread">
    <section class="back-cover">
      <svg class="wave-lines" viewBox="0 0 470 290" preserveAspectRatio="none" aria-hidden="true">
        <path d="M0 250 C 90 210, 170 260, 260 200 S 400 120, 470 60" stroke-width="1.2" opacity=".18"/>
        <path d="M0 268 C 100 230, 180 275, 270 220 S 410 140, 470 90" stroke-width="1" opacity=".14"/>
        <path d="M0 284 C 110 250, 190 290, 280 240 S 420 165, 470 120" stroke-width=".8" opacity=".1"/>
      </svg>

      <h2 class="back-cover__tagline">Believe in you.&nbsp; Trust in You.</h2>
      <div class="back-cover__rule"></div>
      <p class="book-summary">Sip. Stroll. Flourish. is a book committed to you. Behavior change and improved health can be challenging. You must feel empowered to make decisions and changes create momentum in the right direction. But, you may not always have the knowledge to do that. This book provides you with practical and fun tools and tips to improve your nutrition, motivation to move, and mindset. You are awesome. You are beautiful. You have the power to control your destiny and future. All you have to do is Sip, Stroll, and Flourish!</p>

      <div class="author-photo" role="img" aria-label="Black and white portrait photograph of the author"></div>
      <div class="about-author">
        <h3 class="about-author__heading">About the Author</h3>
        <p class="about-author__body">Gregory Talbrecht is a Registered Dietitian and Certified Personal Trainer from Cleveland, OH. He graduated from the Verdant Plains University and currently works as a health coach in the healthcare industry. His passions are fitness, nutrition, science, and motivation. He has extensive knowledge and experience in wellness, healthcare, and disease treatment and disease. Gregory has worked with hundreds of people through counseling, consulting, and coaching in an effort to make a difference in their long-term health. In his spare time, he enjoys exercising, watching movies, and trying out new foods.</p>
      </div>

      <div class="back-brand">
        <span class="brand-name">SSF</span>
        <span class="brand-square"></span>
      </div>
      <p class="back-cover__url">www.sipstrollflourish.com</p>
      <div class="barcode-frame"></div>
    </section>

    <section class="spine">
      <span class="spine__brand brand-name">SSF</span>
      <span class="spine__title">Sip Stroll Flourish</span>
      <span class="spine__author">Gregory Talbrecht</span>
    </section>

    <section class="front-cover">
      <div class="front-cover__scene" role="img" aria-label="Snowy mountain ridge with a hiker climbing toward a bright sun flare"></div>
      <svg class="wave-lines" viewBox="0 0 470 460" preserveAspectRatio="none" aria-hidden="true">
        <path d="M0 330 C 80 280, 160 340, 240 270 S 380 150, 470 110" stroke-width="1.6" opacity=".35"/>
        <path d="M0 352 C 90 305, 170 362, 250 295 S 390 178, 470 140" stroke-width="1.2" opacity=".28"/>
        <path d="M0 374 C 100 330, 180 384, 260 320 S 400 206, 470 170" stroke-width="1" opacity=".22"/>
        <path d="M0 396 C 110 355, 190 406, 270 345 S 410 234, 470 200" stroke-width=".8" opacity=".16"/>
      </svg>
      <div class="front-brand"><span class="brand-name">SSF</span></div>
      <h1 class="front-title">
        <span class="front-title__line1">Sip</span>
        <span class="front-title__line2">Stroll</span>
        <span class="front-title__line3">Flourish</span>
      </h1>
      <p class="front-cover__author">Gregory Talbrecht</p>
    </section>
  </main>
</body>
</html>
```